beauty salon application for consumer

- Find your favorite beauty salons and spas or discover new places next to you with geolocation;
- Filter your search by price, distance, category and type of service;
- Never worry again about having to schedule during your work hours or about not having your calls answered when you want to book an appointment;
- Mark salons as favorites and be the first to be informed of exclusive discounts;
- Don’t ever forget your appointments with Glow Nook’s notifications;
- Compare prices, places and services freely, in a quick and practical way;
- Share reviews about services and places you go with other users and read their opinions;
- USER-FRIENDLY INTERFACE
- GALLERY
- OFFERS

similar interface with application name "primlane"

Industry/Entity Type

Beauty Salon

Font styles to use
Decorative
Script

Colors

Designer to choose colors to be used in the design.

Requirements
Must have
• Please have a look into these applications:
• 1- https://apps.example-store.test/gb/app/primlane/id502918377/?pid=corvella&c=footer-link
• 2- https://apps.example-store.test/us/app/fizz-ltd-book-curl-set-glam-nail-services/id6093817245
• 3- https://market.sample-apps.test/store/apps/details?id=com.lumiparlour.user&hl=en
• 4- https://apps.example-store.test/app/id361720498?mt=8
Nice to have
• Nice to give me a clear screenshots for main function of the application ,please see the above applications before giving me a design .

```html
<!DOCTYPE html>
<html lang="en">
<head>
<meta charset="utf-8">
<title>primlane – salon booking screens</title>
<link rel="stylesheet" href="https://fonts.googleapis.com/css2?family=Mali:wght@400;500&family=Inter:wght@500;600&display=swap">
<style>
:root{
  --bg-top:#ffffff;
  --bg-band:#46425a;
  --mint:#dcefe8;
  --map:#e4eeea;
  --lavender:#f1eef9;
  --panel:#f7f6fb;
  --white:#ffffff;
  --ink:#3a3840;
  --muted:#5e5c66;
  --line:#7a7880;
  --teal:#178e9e;
  --star:#f5c518;
  --purple:#7c5cf6;
  --blue:#1d7cf2;
  --green:#5cc152;
}
*{box-sizing:border-box;margin:0;padding:0}
html,body{width:1200px;height:800px;overflow:hidden}
body{background:linear-gradient(var(--bg-top) 0 416px,var(--bg-band) 416px 800px);font-family:"Mali",sans-serif;color:var(--ink);position:relative}
.screen{position:absolute;top:82px;width:360px;height:640px;overflow:hidden;border-radius:8px;background:var(--lavender);box-shadow:0 6px 18px rgba(0,0,0,.12)}
.s1{left:30px}.s2{left:420px}.s3{left:802px;border-radius:0}
.abs{position:absolute}
.status{position:absolute;left:0;top:0;width:100%;height:26px;font-family:"Inter",sans-serif;font-size:11px;font-weight:600;color:#111;z-index:5}
.status .time{position:absolute;left:0;right:0;top:2px;text-align:center}
.status .sig{position:absolute;left:6px;top:4px}
.status .bat{position:absolute;right:6px;top:2px;display:flex;align-items:center;gap:4px}
.avatar{position:absolute;width:28px;height:28px;border-radius:50%;border:2px solid #fff;background:radial-gradient(circle at 50% 40%,#c99a80,#5a3a2c);z-index:5}
/* dashboard */
.map{position:absolute;left:0;top:0;width:360px;height:278px;background:linear-gradient(180deg,var(--mint) 0%,var(--map) 35%,#eceeec 100%);border-bottom:1px solid #dcdde6}
.map-markers{position:absolute;left:0;top:0;z-index:2}
.hamburger{position:absolute;left:11px;top:33px;z-index:5}
.title{position:absolute;left:0;right:0;top:30px;text-align:center;font-size:17px;color:var(--ink);z-index:5}
.search{position:absolute;left:10px;top:63px;width:340px;height:35px;background:var(--white);border-radius:4px;box-shadow:0 1px 4px rgba(0,0,0,.08);font-size:13px;padding:9px 10px;color:var(--ink);z-index:5}
.search svg{position:absolute;right:10px;top:9px}
.h2{position:absolute;left:11px;font-size:17px;color:var(--ink)}
.cat{position:absolute;top:327px;width:144px;height:99px;border-radius:6px}
.cat .pill{position:absolute;left:22px;right:22px;bottom:12px;height:22px;border-radius:11px;background:var(--white);font-size:12px;text-align:center;line-height:22px}
.card{position:absolute;top:477px;width:231px;height:155px;border-radius:6px;overflow:hidden}
.card .photo{position:absolute;inset:0}
.card .info{position:absolute;left:10px;right:10px;bottom:0;height:62px;background:var(--white);padding:6px 10px}
.card .name{font-size:16px}
.badge{display:inline-block;background:var(--teal);color:#fff;font-size:11px;border-radius:2px;padding:1px 5px}
.card .badge{position:absolute;right:10px;top:6px}
.card .meta{display:flex;gap:10px;font-size:9.5px;line-height:11px;margin-top:4px;color:var(--muted);white-space:nowrap}
/* detail */
.hero{position:absolute;left:0;top:0;width:360px;height:200px;background:linear-gradient(90deg,#b9ccc4 0%,#d8cfc8 45%,#e2e4e2 75%,#c6b7b4 100%)}
.back{position:absolute;left:10px;top:33px;z-index:5}
.salon{position:absolute;left:8px;top:146px;width:344px;height:56px;background:var(--panel);padding:8px 23px;box-shadow:0 1px 3px rgba(0,0,0,.05)}
.salon .name{font-size:17px;line-height:22px}
.salon .addr{font-size:11px;color:var(--muted)}
.salon .rate{position:absolute;right:14px;top:19px;display:flex;align-items:center;gap:6px}
.list{position:absolute;left:10px;top:211px;width:340px;height:430px;background:var(--panel)}
.sec{position:absolute;left:14px;font-size:11px;color:var(--muted);letter-spacing:.2px}
.row{position:absolute;left:0;width:340px;height:52px}
.thumb{position:absolute;left:13px;top:0;width:52px;height:52px;border-radius:50%}
.svc{position:absolute;left:78px;top:15px;font-size:14px}
.price{position:absolute;left:260px;top:11px;width:66px;height:29px;border:1px solid var(--line);border-radius:15px;font-size:14px;display:flex;align-items:center;justify-content:center;gap:5px}
.done{position:absolute;left:260px;top:11px;width:66px;height:29px;border-radius:15px;background:var(--green);display:flex;align-items:center;justify-content:center}
.bottom{position:absolute;left:0;top:586px;width:360px;height:54px;background:var(--white)}
.bottom .note{position:absolute;left:19px;top:18px;font-size:13px}
.btn{position:absolute;background:var(--purple);color:#fff;font-size:13px;display:flex;align-items:center;justify-content:center}
.sheet{position:absolute;left:0;top:486px;width:360px;height:154px;background:var(--white);box-shadow:0 -2px 6px rgba(0,0,0,.06)}
.chip{position:absolute;height:29px;border:1px solid var(--line);border-radius:15px;font-size:12px;display:flex;align-items:center;justify-content:center;white-space:nowrap;overflow:hidden}
.chip.on{background:var(--blue);border-color:var(--blue);color:#fff}
</style>
</head>
<body>

<!-- Dashboard -->
<section class="screen s1">
  <div class="map" role="img" aria-label="Street map of the area around the user with nearby salon markers"></div>
  <svg class="map-markers" width="360" height="278" viewBox="0 0 360 278" aria-hidden="true">
    <circle cx="118" cy="192" r="22" fill="#1d7cf2" fill-opacity=".2"/>
    <circle cx="118" cy="192" r="6" fill="#1d7cf2"/>
    <circle cx="214" cy="132" r="4.5" fill="#1d7cf2"/>
    <circle cx="44" cy="156" r="4.5" fill="#1d7cf2"/>
    <circle cx="324" cy="139" r="4.5" fill="#1d7cf2" fill-opacity=".5"/>
    <circle cx="32" cy="222" r="4.5" fill="#1d7cf2"/>
    <circle cx="246" cy="221" r="4.5" fill="#1d7cf2"/>
    <circle cx="156" cy="249" r="4.5" fill="#1d7cf2"/>
  </svg>
  <div class="status">
    <svg class="sig" width="34" height="10" viewBox="0 0 34 10"><rect x="0" y="6" width="3" height="4" fill="#111"/><rect x="4" y="4" width="3" height="6" fill="#111"/><rect x="8" y="2" width="3" height="8" fill="#111"/><rect x="12" y="0" width="3" height="10" fill="#111"/><path d="M19 4a8 8 0 0 1 12 0M21.5 6.5a4.5 4.5 0 0 1 7 0" stroke="#111" stroke-width="1.6" fill="none"/><circle cx="25" cy="9" r="1.2" fill="#111"/></svg>
    <div class="time">9:41 AM</div>
    <div class="bat"><span>✱ 100%</span><svg width="24" height="11" viewBox="0 0 24 11"><rect x=".5" y=".5" width="21" height="10" rx="2" fill="none" stroke="#111"/><rect x="2" y="2" width="18" height="7" rx="1" fill="#111"/><rect x="22" y="3.5" width="1.5" height="4" fill="#111"/></svg></div>
  </div>
  <svg class="hamburger" width="17" height="14" viewBox="0 0 17 14"><path d="M0 1h17M0 7h17M0 13h17" stroke="#222" stroke-width="1.6"/></svg>
  <div class="title">Dashboard</div>
  <div class="avatar" role="img" aria-label="User profile photo" style="left:324px;top:25px"></div>
  <div class="search">New Delhi, India
    <svg width="16" height="16" viewBox="0 0 16 16"><circle cx="6.5" cy="6.5" r="5.5" stroke="#777" stroke-width="1.4" fill="none"/><path d="M10.5 10.5L15 15" stroke="#777" stroke-width="1.4"/></svg>
  </div>
  <div class="h2" style="top:293px">Categories</div>
  <svg class="abs" style="left:339px;top:298px" width="16" height="15" viewBox="0 0 16 15"><path d="M0 2h16M0 7.5h16M0 13h16" stroke="#555" stroke-width="1"/><circle cx="4" cy="2" r="1.8" fill="#f1eef9" stroke="#555"/><circle cx="11" cy="7.5" r="1.8" fill="#f1eef9" stroke="#555"/><circle cx="5" cy="13" r="1.8" fill="#f1eef9" stroke="#555"/></svg>
  <div class="cat" role="img" aria-label="Hair salon category photo" style="left:11px;background:linear-gradient(135deg,#8c8c90,#c9bfb8)"><div class="pill">Hair Salon</div></div>
  <div class="cat" role="img" aria-label="Wax and spa category photo" style="left:165px;background:linear-gradient(135deg,#cfe4e6,#b56a4a)"><div class="pill">Wax &amp; Spa</div></div>
  <div class="cat" role="img" aria-label="Further category photo" style="left:319px;background:linear-gradient(135deg,#6f8a72,#9fb0a4)"></div>
  <div class="h2" style="top:443px">Hair Salon</div>
  <div class="card" style="left:11px">
    <div class="photo" role="img" aria-label="Salon promotional photo" style="background:linear-gradient(90deg,#8ea89a,#c9b7ac 55%,#9a7a70)"></div>
    <div class="info">
      <div class="name">Luma &amp; Co Salon</div><span class="badge">4.7</span>
      <div class="meta"><span>⚲ 48 C Marlow Lane<br>London B7K TQ2</span><span>Hair, Spa, Salon<br>Wax, Others</span></div>
    </div>
  </div>
  <div class="card" style="left:253px">
    <div class="photo" role="img" aria-label="Salon promotional photo" style="background:linear-gradient(90deg,#d7e6ea,#b9643f)"></div>
    <div class="info"><div class="name">Velvet Roo</div><div class="meta"><span>⚲ 48 C Marlow<br>London B7K</span></div></div>
  </div>
</section>

<!-- Salon detail -->
<section class="screen s2">
  <div class="hero" role="img" aria-label="Salon cover photo"></div>
  <div class="status">
    <svg class="sig" width="34" height="10" viewBox="0 0 34 10"><rect x="0" y="6" width="3" height="4" fill="#111"/><rect x="4" y="4" width="3" height="6" fill="#111"/><rect x="8" y="2" width="3" height="8" fill="#111"/><rect x="12" y="0" width="3" height="10" fill="#111"/><path d="M19 4a8 8 0 0 1 12 0M21.5 6.5a4.5 4.5 0 0 1 7 0" stroke="#111" stroke-width="1.6" fill="none"/><circle cx="25" cy="9" r="1.2" fill="#111"/></svg>
    <div class="time">9:41 AM</div>
    <div class="bat"><span>✱ 100%</span><svg width="24" height="11" viewBox="0 0 24 11"><rect x=".5" y=".5" width="21" height="10" rx="2" fill="none" stroke="#111"/><rect x="2" y="2" width="18" height="7" rx="1" fill="#111"/><rect x="22" y="3.5" width="1.5" height="4" fill="#111"/></svg></div>
  </div>
  <svg class="back" width="20" height="16" viewBox="0 0 20 16"><path d="M19 8H2M8 1L1 8l7 7" stroke="#222" stroke-width="1.6" fill="none"/></svg>
  <div class="avatar" role="img" aria-label="User profile photo" style="left:323px;top:25px"></div>
  <div class="salon"><div class="name">Luma &amp; Co Salon</div><div class="addr">48 C Marlow Lane London B7K TQ2</div>
    <div class="rate"><svg width="14" height="14" viewBox="0 0 24 24"><path d="M12 2l3 6.9 7.5.7-5.7 5 1.7 7.4L12 18l-6.5 4 1.7-7.4-5.7-5 7.5-.7z" fill="var(--star)"/></svg><span class="badge">4.7</span></div>
  </div>
  <div class="list">
    <div class="sec" style="top:16px">HAIR CARE</div>
    <div class="row" style="top:37px"><div class="thumb" role="img" aria-label="Hair straightening photo" style="background:linear-gradient(135deg,#5a3a22,#c7a27c)"></div><div class="svc">Hair straightening</div><div class="price">+ $24</div></div>
    <div class="row" style="top:103px"><div class="thumb" role="img" aria-label="Hair curling photo" style="background:linear-gradient(135deg,#2c2622,#d7b7a6)"></div><div class="svc">Hair Curling</div><div class="price">+ $44</div></div>
    <div class="row" style="top:169px"><div class="thumb" role="img" aria-label="Waxing photo" style="background:linear-gradient(135deg,#efe9e2,#d2b49a)"></div><div class="svc">Waxing</div><div class="price">+ $54</div></div>
    <div class="sec" style="top:236px">FACIAL</div>
    <div class="row" style="top:256px"><div class="thumb" role="img" aria-label="Facial pack photo" style="background:linear-gradient(135deg,#2e2a28,#b69080)"></div><div class="svc">Facial Pack</div><div class="price">+ $24</div></div>
    <div class="row" style="top:322px"><div class="thumb" role="img" aria-label="Hair curling photo" style="background:linear-gradient(135deg,#cfe3ea,#c0704e)"></div><div class="svc">Hair Curling</div><div class="price">+ $44</div></div>
  </div>
  <div class="bottom"><div class="note">No Bookings to Show</div><div class="btn" style="left:219px;top:9px;width:133px;height:38px">Book Now</div></div>
</section>

<!-- Booking selection -->
<section class="screen s3">
  <div class="hero" role="img" aria-label="Salon cover photo"></div>
  <div class="status">
    <svg class="sig" width="34" height="10" viewBox="0 0 34 10"><rect x="0" y="6" width="3" height="4" fill="#111"/><rect x="4" y="4" width="3" height="6" fill="#111"/><rect x="8" y="2" width="3" height="8" fill="#111"/><rect x="12" y="0" width="3" height="10" fill="#111"/><path d="M19 4a8 8 0 0 1 12 0M21.5 6.5a4.5 4.5 0 0 1 7 0" stroke="#111" stroke-width="1.6" fill="none"/><circle cx="25" cy="9" r="1.2" fill="#111"/></svg>
    <div class="time">9:41 AM</div>
    <div class="bat"><span>✱ 100%</span><svg width="24" height="11" viewBox="0 0 24 11"><rect x=".5" y=".5" width="21" height="10" rx="2" fill="none" stroke="#111"/><rect x="2" y="2" width="18" height="7" rx="1" fill="#111"/><rect x="22" y="3.5" width="1.5" height="4" fill="#111"/></svg></div>
  </div>
  <svg class="back" width="20" height="16" viewBox="0 0 20 16"><path d="M19 8H2M8 1L1 8l7 7" stroke="#222" stroke-width="1.6" fill="none"/></svg>
  <div class="avatar" role="img" aria-label="User profile photo" style="left:323px;top:25px"></div>
  <div class="salon"><div class="name">Luma &amp; Co Salon</div><div class="addr">48 C Marlow Lane London B7K TQ2</div>
    <div class="rate"><svg width="14" height="14" viewBox="0 0 24 24"><path d="M12 2l3 6.9 7.5.7-5.7 5 1.7 7.4L12 18l-6.5 4 1.7-7.4-5.7-5 7.5-.7z" fill="var(--star)"/></svg><span class="badge">4.7</span></div>
  </div>
  <div class="list">
    <div class="sec" style="top:16px">HAIR CARE</div>
    <div class="row" style="top:37px"><div class="thumb" role="img" aria-label="Hair straightening photo" style="background:linear-gradient(135deg,#5a3a22,#c7a27c)"></div><div class="svc">Hair straightening</div><div class="done"><svg width="18" height="14" viewBox="0 0 18 14"><path d="M1 7l5 5L17 1" stroke="#fff" stroke-width="1.6" fill="none"/></svg></div></div>
    <div class="row" style="top:103px"><div class="thumb" role="img" aria-label="Hair curling photo" style="background:linear-gradient(135deg,#2c2622,#d7b7a6)"></div><div class="svc">Hair Curling</div><div class="price">+ $44</div></div>
    <div class="row" style="top:169px"><div class="thumb" role="img" aria-label="Waxing photo" style="background:linear-gradient(135deg,#efe9e2,#d2b49a)"></div><div class="svc">Waxing</div><div class="price">+ $54</div></div>
    <div class="sec" style="top:236px">FACIAL</div>
    <div class="row" style="top:256px"><div class="thumb" role="img" aria-label="Facial pack photo" style="background:linear-gradient(135deg,#2e2a28,#b69080)"></div></div>
  </div>
  <div class="sheet">
    <div class="chip" style="left:10px;top:18px;width:59px">Sat 30</div>
    <div class="chip" style="left:77px;top:18px;width:59px">Sun 31</div>
    <div class="chip on" style="left:143px;top:18px;width:59px">Mon 30</div>
    <div class="chip" style="left:210px;top:18px;width:59px">Tue 31</div>
    <div class="chip" style="left:276px;top:18px;width:59px">Wed 30</div>
    <div class="chip" style="left:342px;top:18px;width:40px;justify-content:flex-start;padding-left:10px">T</div>
    <div class="chip" style="left:1px;top:63px;width:78px">11:00 - 12:00</div>
    <div class="chip on" style="left:85px;top:63px;width:86px">12:00 - 01:00</div>
    <div class="chip" style="left:178px;top:63px;width:86px">01:00 - 02:00</div>
    <div class="chip" style="left:271px;top:63px;width:86px">03:00 - 04:00</div>
    <div class="btn" style="left:10px;top:108px;width:340px;height:38px">Book Now</div>
  </div>
</section>

</body>
</html>
```